Business Cards for GPS Technology Business - Logo Supplied

Varel Systems Ltd. requires a business card design. Varel is a startup GPS vehicle fleet tracking vendor. Our hardware/software helps business fleets be more productive and reduce operating costs. Our systems utilize a mix of GPS satellite, cell network and web technologies.
We would like to see a double sided original design utilizing our existing logo. Please use whatever colors will work with the blue logo.
As a business, we want to project the image of friendly and approachable lifetime business partners and advisors to our customers - “someone you can trust”. Words customers will use to describe us will include: knowledgeable, supportive, trustworthy and honest.
We will also require Vidplex, Chirpa, Frendly and Lumo+ backgrounds. Winner will be first in line to quote for this work (separate project).
Target Market(s)
Target audience are working owners and managers of vehicle fleets. Usually male, age 30 to 60. Often have a trades background.
Industry/Entity Type
Business
Font styles to use
Requirements
Must have
- Please use the following dummy data for the design:
name: Tim Varel
title: Director
address: 2381 Calden Lane
city: Sommetown, BC
postal code: K7P 2W4
cell phone number: 555-214-7390
business number: 555-318-4602
toll free number: 1-800-555-0193
web site address: www.varel-example.com
tagline: GPS Fleet Tracking Specialists
Nice to have
- Abstract imagery relating to GPS tracking / fleet vehicles / technology
Should not have
- Do not use serif fonts.

```html
<!DOCTYPE html>
<html lang="en">
<head>
<meta charset="utf-8">
<title>Varel Systems Ltd. – Business Card</title>
<link rel="stylesheet" href="https://fonts.googleapis.com/css2?family=Open+Sans:wght@400;600;800&display=swap">
<style>
  :root {
    --brand-blue: #1b6bb8;
    --paper: #ffffff;
    --paper-shade: #e4e6e9;
    --ink: #4a4d52;
    --backdrop: #d9dbde;
  }
  html, body {
    margin: 0;
    width: 1200px;
    height: 939px;
    overflow: hidden;
    background: var(--backdrop);
    font-family: "Open Sans", Arial, sans-serif;
  }
  .canvas { position: relative; width: 1200px; height: 939px; }
  .card {
    position: absolute;
    width: 540px;
    height: 309px;
    box-shadow: 0 6px 18px rgba(0,0,0,.22);
    background: var(--paper);
  }
  .card svg { display: block; width: 100%; height: 100%; }
  .card--front { left: 100px; top: 110px; }
  .card--back { left: 560px; top: 520px; }
  .brand-blue { fill: var(--brand-blue); }
  .paper-fill { fill: url(#paperGrad); }
  .logo-word { font-family: "Open Sans", Arial, sans-serif; font-weight: 800; letter-spacing: 1px; }
  .logo-word--light { fill: var(--paper); }
  .logo-word--blue { fill: var(--brand-blue); }
  .tagline { fill: var(--paper); font-family: "Open Sans", Arial, sans-serif; font-weight: 600; font-size: 15px; }
  .person-name { fill: var(--ink); font-family: "Open Sans", Arial, sans-serif; font-weight: 600; font-size: 15px; }
  .person-title { fill: var(--ink); font-family: "Open Sans", Arial, sans-serif; font-weight: 400; font-size: 15px; }
  .contact { fill: var(--ink); font-family: "Open Sans", Arial, sans-serif; font-size: 9.5px; }
  .contact-icon { fill: var(--ink); }
  .social-label { fill: var(--brand-blue); font-family: "Open Sans", Arial, sans-serif; font-weight: 600; font-size: 10px; }
</style>
</head>
<body>
<div class="canvas">

  <svg width="0" height="0" style="position:absolute">
    <defs>
      <linearGradient id="paperGrad" x1="0" y1="0" x2="1" y2="1">
        <stop offset="0" stop-color="#ffffff"/>
        <stop offset="1" stop-color="#e4e6e9"/>
      </linearGradient>
    </defs>
  </svg>

  <!-- Front side -->
  <div class="card card--front">
    <svg viewBox="0 0 540 309" aria-label="Front of business card">
      <rect class="brand-blue" width="540" height="309"/>
      <path class="paper-fill" d="M0,0 H262 V28 Q262,76 214,76 H0 Z"/>
      <path class="paper-fill" d="M318,309 Q500,250 540,88 V309 Z"/>
      <text class="logo-word logo-word--light" x="28" y="222" font-size="46">varel</text>
      <text class="tagline" x="28" y="252">GPS Fleet Tracking Specialists</text>
    </svg>
  </div>

  <!-- Back side -->
  <div class="card card--back">
    <svg viewBox="0 0 540 309" aria-label="Back of business card">
      <rect class="paper-fill" width="540" height="309"/>
      <path class="brand-blue" d="M0,0 H150 Q50,80 38,309 H0 Z"/>
      <path class="brand-blue" d="M232,309 V262 Q232,212 282,212 H540 V309 Z"/>

      <text text-anchor="end" x="512" y="52">
        <tspan class="person-name">Tim Varel</tspan>
        <tspan class="person-title"> | Director</tspan>
      </text>
      <text class="logo-word logo-word--blue" text-anchor="end" x="512" y="112" font-size="60">varel</text>

      <g class="contact-lines">
        <circle class="contact-icon" cx="254" cy="145" r="3.5"/>
        <text class="contact" x="261" y="148">555-214-7390</text>
        <circle class="contact-icon" cx="340" cy="145" r="3.5"/>
        <text class="contact" x="347" y="148">555-318-4602</text>
        <circle class="contact-icon" cx="426" cy="145" r="3.5"/>
        <text class="contact" x="512" y="148" text-anchor="end">1-800-555-0193</text>
        <circle class="contact-icon" cx="166" cy="161" r="3.5"/>
        <text class="contact" x="173" y="164">2381 Calden Lane, Sommetown, BC K7P 2W4</text>
        <circle class="contact-icon" cx="386" cy="161" r="3.5"/>
        <text class="contact" x="512" y="164" text-anchor="end">www.varel-example.com</text>
      </g>

      <g class="social-row">
        <rect class="brand-blue" x="62" y="259" width="8" height="8"/>
        <text class="social-label" x="73" y="267">Vidplex</text>
        <rect class="brand-blue" x="62" y="276" width="8" height="8"/>
        <text class="social-label" x="73" y="284">Chirpa</text>
        <rect class="brand-blue" x="122" y="259" width="8" height="8"/>
        <text class="social-label" x="133" y="267">Frendly</text>
        <rect class="brand-blue" x="122" y="276" width="8" height="8"/>
        <text class="social-label" x="133" y="284">Lumo+</text>
      </g>
    </svg>
  </div>

</div>
</body>
</html>
```